Veradine Contracting Folder

Creating a design for the cover of our folders that we pass to our customers

Want to keep the same look as our colors and fonts as attached

```html
<!DOCTYPE html>
<html lang="en">
<head>
<meta charset="utf-8">
<title>Veradine Contracting Folder</title>
<link rel="stylesheet" href="https://fonts.googleapis.com/css2?family=Didact+Gothic&display=swap">
<style>
  :root {
    --gold-deep: #bb8400;
    --gold-mid: #dcab1e;
    --gold-light: #fcd435;
    --royal-blue: #1010a8;
    --lavender: #a9a9dc;
    --paper: #ffffff;
    --trim: #b8b8b8;
    --fold: #8a6a2a;
    --paint-white: #f7f3ea;
    --overall-beige: #c9b79c;
    --ladder-blue: #2a2ab0;
  }
  * { margin: 0; padding: 0; box-sizing: border-box; }
  html, body { width: 1200px; height: 891px; overflow: hidden; background: var(--paper); }
  body { position: relative; font-family: "Didact Gothic", "Century Gothic", sans-serif; }

  .crop-marks { position: absolute; inset: 0; }

  .folder {
    position: absolute;
    left: 88px; top: 84px;
    width: 1021px; height: 696px;
    border: 1px solid var(--trim);
    background: var(--paper);
  }
  .gold-panel {
    position: absolute;
    left: 0; top: 0;
    width: 737px; height: 100%;
    background: linear-gradient(90deg, var(--gold-deep) 0%, var(--gold-mid) 55%, var(--gold-light) 100%);
  }
  .fold-line {
    position: absolute;
    left: 529px; top: -6px; bottom: -32px;
    border-left: 1px dashed var(--fold);
  }

  .brand {
    position: absolute;
    display: flex; align-items: center; gap: 5px;
    height: 44px;
    color: var(--royal-blue);
    font-size: 34px; line-height: 1;
    letter-spacing: 0.5px;
    white-space: nowrap;
  }
  .brand-square {
    width: 8px; height: 42px;
    background: var(--lavender);
  }
  .brand--back { left: 173px; top: 312px; }
  .brand--front { left: 826px; top: 312px; }

  .tagline {
    position: absolute;
    left: 120px; top: 364px;
    width: 296px;
    text-align: center;
    color: var(--paper);
    font-size: 23px;
    letter-spacing: 2.4px;
    white-space: nowrap;
  }

  .painter-art {
    position: absolute;
    left: 610px; top: 436px;
    width: 182px; height: 260px;
  }

  .contact {
    position: absolute;
    color: var(--royal-blue);
    font-style: normal;
    font-size: 9.5px; line-height: 12px;
    white-space: nowrap;
  }
  .contact--address { left: 21px; top: 645px; }
  .contact--lines { left: 357px; top: 648px; }
</style>
</head>
<body>
  <svg class="crop-marks" width="1200" height="891" viewBox="0 0 1200 891" aria-hidden="true">
    <g stroke="#b8b8b8" stroke-width="1">
      <line x1="88" y1="42" x2="88" y2="72"/>
      <line x1="1109" y1="42" x2="1109" y2="72"/>
      <line x1="88" y1="792" x2="88" y2="824"/>
      <line x1="1109" y1="792" x2="1109" y2="824"/>
      <line x1="45" y1="84" x2="74" y2="84"/>
      <line x1="1123" y1="84" x2="1152" y2="84"/>
      <line x1="45" y1="780" x2="74" y2="780"/>
      <line x1="1123" y1="780" x2="1152" y2="780"/>
    </g>
  </svg>

  <section class="folder">
    <div class="gold-panel"></div>
    <div class="fold-line"></div>

    <div class="brand brand--back">
      <span class="brand-square"></span>
      <span class="brand-name">VERADINE</span>
    </div>
    <p class="tagline">Painting &amp; Contracting</p>

    <svg class="painter-art" viewBox="0 0 182 260" role="img" aria-label="Illustration of a house painter on a blue step ladder brushing white paint onto the wall">
      <defs>
        <linearGradient id="painterTone" x1="0" y1="0" x2="1" y2="1">
          <stop offset="0" stop-color="var(--paint-white)"/>
          <stop offset="0.55" stop-color="var(--overall-beige)"/>
          <stop offset="1" stop-color="var(--ladder-blue)"/>
        </linearGradient>
      </defs>
      <rect x="0" y="0" width="182" height="260" rx="14" fill="url(#painterTone)" opacity="0.55"/>
    </svg>

    <address class="contact contact--address">
      Office &amp; Warehouse<br>
      4120 (Rt. 9) Harbor Pkwy<br>
      Lakemont, VA 22410
    </address>
    <address class="contact contact--lines">
      Telephone: (555) 014-0205<br>
      Fax: (555) 014-5439<br>
      Email: info@veradinepainting.com
    </address>

    <div class="brand brand--front">
      <span class="brand-square"></span>
      <span class="brand-name">VERADINE</span>
    </div>
  </section>
</body>
</html>
```